Business Postcard Mailer - 2 sided - 6 x 10.5 inches

We will be purchasing multiple designs through this project. We need a postcard mailer for a residential painting business. The final design needs to have the special 15% Off, contact information, company logo, stamp indicia, and list of services. I will provide past examples and any additional logos. Company colors are #34482E and #4A1717. Old samples are provided. Final flat size should be 6 x 10.5 inches. And we will need a return address in the upper left-hand corner of the backside. QMRB Layout Guidelines are attached. 4389 Juniper Ave #7, Waukesha, WI 53947.
Updates

I just guaranteed the project and will be expecting more entries. We will also be purchasing additional designs (4-5) so we want to ensure a good variety.

Target Market(s)

Homeowners

Industry/Entity Type

Painting

Font styles to use
Sans Serif

Requirements
Must have
• Logo and brand colors
Nice to have
• Call to action - Book your free estimate at www.BrightCoatCrew.example or Call now 262-555-0147.

```html
<!DOCTYPE html>
<html lang="en">
<head>
<meta charset="utf-8">
<title>Bright Coat Crew – Postcard Mailer</title>
<link rel="stylesheet" href="https://fonts.googleapis.com/css2?family=Oswald:wght@500&family=Cabin:wght@500;600&family=Montserrat:wght@700;800&family=Arimo:wght@400;700&display=swap">
<style>
:root{
  --green:#34482E;
  --red:#4A1717;
  --red-soft:#5e1f1f;
  --white:#ffffff;
  --ink:#1c1c1c;
  --bg:#d9d9d9;
  --indicia:#bdbdbd;
}
*{box-sizing:border-box;margin:0;padding:0}
html,body{width:1200px;height:1200px;overflow:hidden}
body{background:var(--bg);position:relative;font-family:"Cabin",sans-serif;color:var(--ink)}
.card{position:absolute;background:var(--white);overflow:hidden}
.card--front{left:66px;top:59px;width:893px;height:509px}
.card--back{left:250px;top:619px;width:893px;height:509px}
.abs{position:absolute}
.photo{position:absolute}
.photo--house{left:14px;top:12px;width:864px;height:351px;background:linear-gradient(180deg,#d6d8da 0%,#5b6470 40%,#6d6a62 62%,#5d8a3c 85%,#4d7a30 100%)}
.thumbs{left:410px;top:252px;width:438px;height:111px;background:var(--white)}
.thumb{position:absolute;top:9px;width:136px;height:101px}
.thumb--deck{left:8px;background:linear-gradient(180deg,#c8c8c8,#8a6a4d 55%,#6e4c33)}
.thumb--ranch{left:144px;background:linear-gradient(180deg,#c9ccd0,#8d8a82 50%,#6e9a4a 80%)}
.thumb--farm{left:286px;background:linear-gradient(180deg,#b9c3cc,#e6e6e2 55%,#889a78)}
.services{background:var(--green);color:var(--white)}
.services--front{left:560px;top:0;width:288px;height:252px;padding:22px 0 0 22px}
.services__title{font-family:"Oswald",sans-serif;font-weight:500;text-transform:uppercase;letter-spacing:.2px;line-height:1}
.services--front .services__title{font-size:33px;margin-bottom:10px}
.services__list{list-style:none}
.services__item{display:flex;align-items:center;font-weight:500}
.services--front .services__item{font-size:20.5px;height:33px}
.tick{flex:none;margin-right:12px}
.services__note{font-size:8.5px;margin-top:6px}
.logo{display:flex;align-items:center;gap:8px;font-family:"Montserrat",sans-serif;font-weight:800;line-height:1.02}
.logo__mark{flex:none;width:16px;height:16px}
.logo--front{left:14px;top:400px;width:230px;color:var(--red);font-size:27px}
.logo--front .logo__mark{background:var(--green)}
.divider{left:254px;top:380px;width:2px;height:112px;background:#e3e3e3}
.cta--front{left:270px;top:390px;width:280px;text-align:center}
.cta__lead{font-size:15px;font-weight:500}
.cta__phone{font-family:"Montserrat",sans-serif;font-weight:800;letter-spacing:-.5px;line-height:1.05}
.cta--front .cta__phone{font-size:38px}
.cta__web{display:inline-block;font-family:"Montserrat",sans-serif;font-weight:700;color:var(--white);border-radius:5px}
.cta--front .cta__web{background:var(--green);font-size:14.5px;padding:7px 10px;margin-top:4px;width:275px}
.offer{left:560px;top:370px;width:288px;height:126px;background:var(--red);color:var(--white);padding:10px 12px}
.offer__frame{border:2px dashed var(--white);height:100%;text-align:center;font-family:"Montserrat",sans-serif;padding-top:11px}
.offer__kicker{font-weight:700;font-size:13px}
.offer__big{font-weight:800;font-size:51px;line-height:1}
.offer__sub{font-weight:700;font-size:12.5px;margin-top:2px}

/* back */
.services--back{left:12px;top:11px;width:198px;height:214px;background:var(--red);padding:24px 0 0 14px}
.services--back .services__title{font-size:25px;margin-bottom:6px}
.services--back .services__item{font-size:16px;height:26px}
.photo--room{left:210px;top:11px;width:276px;height:214px;background:linear-gradient(160deg,#f1f0ee 0%,#dcd7d0 45%,#a7a29b 75%,#7e7c7c 100%)}
.band{left:12px;width:474px}
.band--crew{top:225px;height:132px;background:var(--green);color:var(--white);text-align:center;padding-top:17px}
.band__text{font-size:13.5px;line-height:1.3;font-weight:500}
.badges{display:flex;justify-content:center;gap:18px;margin-top:18px}
.badge{height:40px;border:2px solid rgba(255,255,255,.85);border-radius:4px}
.band--contact{top:357px;height:38px;background:var(--red);color:var(--white);font-family:"Montserrat",sans-serif;font-weight:800;font-size:20px;text-align:center;line-height:38px}
.band--footer{top:395px;height:100px;background:var(--green)}
.logo--back{left:30px;top:20px;width:170px;color:var(--white);font-size:22px}
.logo--back .logo__mark{background:var(--white)}
.cta--back{right:14px;top:14px;text-align:right;color:var(--white)}
.cta--back .cta__lead{font-size:11px}
.cta--back .cta__phone{font-size:27px}
.cta--back .cta__web{background:var(--red);font-size:15px;padding:5px 10px;margin-top:3px}
.return{left:505px;top:45px;font-size:14px;font-weight:500;line-height:1.35}
.indicia{left:797px;top:11px;width:82px;height:102px;background:var(--indicia);font-family:"Arimo",sans-serif;font-size:11.5px;text-align:center;padding-top:12px;line-height:1.25}
.indicia__paid{font-weight:700;font-size:16px;margin:4px 0 2px}
.address-line{left:505px;width:373px;height:1px;background:var(--ink)}
</style>
</head>
<body>

<svg width="0" height="0" style="position:absolute" aria-hidden="true">
  <symbol id="tick" viewBox="0 0 24 22">
    <rect x="1.5" y="5" width="15" height="15" fill="none" stroke="currentColor" stroke-width="2"/>
    <path d="M5 12 l4 5 L22 2" fill="none" stroke="currentColor" stroke-width="2.6" stroke-linecap="round" stroke-linejoin="round"/>
  </symbol>
</svg>

<!-- Front side -->
<section class="card card--front">
  <div class="photo photo--house" role="img" aria-label="Photo of a two-storey house with dark blue siding and stone accents"></div>

  <div class="abs services services--front">
    <h2 class="services__title">Our Services</h2>
    <ul class="services__list">
      <li class="services__item"><svg class="tick" width="24" height="22"><use href="#tick"/></svg>Interior Painting</li>
      <li class="services__item"><svg class="tick" width="24" height="22"><use href="#tick"/></svg>Exterior Painting</li>
      <li class="services__item"><svg class="tick" width="24" height="22"><use href="#tick"/></svg>Carpentry Services</li>
      <li class="services__item"><svg class="tick" width="24" height="22"><use href="#tick"/></svg>Drywall Repair</li>
      <li class="services__item"><svg class="tick" width="24" height="22"><use href="#tick"/></svg>Color Consultations</li>
    </ul>
    <p class="services__note">Locally Owned and Operated</p>
  </div>

  <div class="abs thumbs">
    <div class="thumb thumb--deck" role="img" aria-label="Photo of a painter refinishing a wooden deck"></div>
    <div class="thumb thumb--ranch" role="img" aria-label="Photo of a freshly painted ranch home"></div>
    <div class="thumb thumb--farm" role="img" aria-label="Photo of a white farmhouse being repainted"></div>
  </div>

  <div class="abs logo logo--front"><span class="logo__mark"></span><span>Bright Coat Crew</span></div>
  <div class="abs divider"></div>

  <div class="abs cta cta--front">
    <p class="cta__lead">Book your free estimate at</p>
    <p class="cta__phone">262-555-0147</p>
    <span class="cta__web">www.BrightCoatCrew.example</span>
  </div>

  <div class="abs offer">
    <div class="offer__frame">
      <p class="offer__kicker">Fall Special</p>
      <p class="offer__big">15% OFF</p>
      <p class="offer__sub">while openings are still available</p>
    </div>
  </div>
</section>

<!-- Back side -->
<section class="card card--back">
  <div class="abs services services--back">
    <h2 class="services__title">Our Services</h2>
    <ul class="services__list">
      <li class="services__item"><svg class="tick" width="20" height="18"><use href="#tick"/></svg>Interior Painting</li>
      <li class="services__item"><svg class="tick" width="20" height="18"><use href="#tick"/></svg>Exterior Painting</li>
      <li class="services__item"><svg class="tick" width="20" height="18"><use href="#tick"/></svg>Carpentry Services</li>
      <li class="services__item"><svg class="tick" width="20" height="18"><use href="#tick"/></svg>Drywall Repair</li>
      <li class="services__item"><svg class="tick" width="20" height="18"><use href="#tick"/></svg>Color Consultations</li>
    </ul>
  </div>
  <div class="photo photo--room" role="img" aria-label="Photo of a bright living room with fireplace and grey sofas"></div>

  <div class="abs band band--crew">
    <p class="band__text">We cater the size of the crew to the size of the job and work full<br>continuous days until the project is complete.</p>
    <div class="badges" aria-label="Association memberships">
      <span class="badge" style="width:34px"></span>
      <span class="badge" style="width:36px"></span>
      <span class="badge" style="width:66px"></span>
      <span class="badge" style="width:50px"></span>
      <span class="badge" style="width:80px"></span>
      <span class="badge" style="width:56px"></span>
    </div>
  </div>

  <div class="abs band band--contact">CONTACT US TODAY!</div>

  <div class="abs band band--footer">
    <div class="abs logo logo--back"><span class="logo__mark"></span><span>Bright Coat Crew</span></div>
    <div class="abs cta cta--back">
      <p class="cta__lead">Book your free estimate at</p>
      <p class="cta__phone">262-555-0147</p>
      <span class="cta__web">www.BrightCoatCrew.example</span>
    </div>
  </div>

  <address class="abs return" style="font-style:normal">4389 Juniper Ave #7,<br>Waukesha, WI 53947</address>

  <div class="abs indicia">
    Presorted<br>Standard<br>U.S. Postage
    <p class="indicia__paid">PAID</p>
    PMX
  </div>

  <div class="abs address-line" style="top:262px"></div>
  <div class="abs address-line" style="top:308px"></div>
  <div class="abs address-line" style="top:354px"></div>
  <div class="abs address-line" style="top:400px"></div>
</section>

</body>
</html>
```